Corporate Design für ein Kfz-Sachverständigenbüro
Zielgruppe
Sachverständiger/Gutachter für Unfallschäden in Kfz-Bereich.
Aufgabenstellung
Hochwertiges neutrales/seriöses Design.
Das Logo/Slogan soll gut im Briefkopf zu Geltung kommen und eher linear/schmal gehalten sein.
Die Fußzeile soll aus Firmenanschrift, Telefon, Email, Website bestehen (keine Steuernummer, Bankverbindung etc. ).
Das Firmenlogo evtl. links neben den Slogan einbringen und evtl. in einer kleineren Schriftgröße.
Firmenname: Kfz-Sachverständigenbüro Lindqvist
Slogan: 'Ihr Sachverständiger & Kfz-Techniker-Meister für Kraftfahrzeugschäden und -bewertung'

```html
<!DOCTYPE html>
<html lang="de">
<head>
<meta charset="utf-8">
<title>Kfz-Sachverständigenbüro Lindqvist – Geschäftsausstattung</title>
<link href="https://fonts.googleapis.com/css2?family=Montserrat:wght@400;500;700;800&display=swap" rel="stylesheet">
<style>
  :root{
    --navy:#283479;
    --dark:#3b3b3b;
    --text:#3f3f3f;
    --muted:#6b6b6b;
    --paper:#ffffff;
    --bg:#ffffff;
  }
  *{box-sizing:border-box;margin:0;padding:0}
  html,body{width:1175px;height:1200px;overflow:hidden;background:var(--bg)}
  body{position:relative;font-family:'Montserrat',sans-serif;color:var(--text)}

  .sheet{position:absolute;background:var(--paper);box-shadow:0 2px 14px rgba(0,0,0,.08);overflow:hidden}
  .band{position:absolute;left:0;width:100%;display:block}

  .brand-mark{position:absolute;border:3px solid var(--navy);border-radius:50%}
  .brand-name{position:absolute;font-weight:800;color:var(--navy);white-space:nowrap;letter-spacing:.01em}
  .brand-slogan{position:absolute;color:var(--muted);white-space:nowrap}

  /* Briefbogen */
  .letter{left:465px;top:212px;width:560px;height:793px}
  .letter .brand-mark{left:65px;top:38px;width:36px;height:36px;border-width:3px}
  .letter .brand-name{left:112px;top:36px;font-size:13.5px}
  .letter .brand-slogan{left:112px;top:55px;font-size:9.6px;line-height:11.5px}
  .letter-body{position:absolute;left:67px;top:296px;width:400px;font-size:8.3px;line-height:14.1px;color:var(--text)}
  .letter-body p{margin-bottom:14px}
  .letter-body .closing{margin-bottom:14px}
  .signature{position:absolute;left:65px;top:582px;width:133px;height:31px;border-radius:4px;background:linear-gradient(90deg,rgba(40,90,200,.18),rgba(40,90,200,.06))}
  .letter-footer{position:absolute;left:67px;top:726px;width:460px;height:50px;font-size:7.4px;line-height:10.4px;color:var(--muted)}
  .letter-footer .company{position:absolute;left:0;top:0;text-transform:uppercase}
  .letter-footer .address{position:absolute;left:0;top:14px}
  .letter-footer .online{position:absolute;left:93px;top:24px}
  .letter-footer .phone{position:absolute;left:198px;top:34px}
  .ico{display:inline-block;vertical-align:-1px;margin-right:3px}
  .letter .band{bottom:0;height:12px}

  /* Visitenkarte Vorderseite */
  .card-front{left:186px;top:403px;width:303px;height:195px}
  .card-front .brand-mark{left:29px;top:34px;width:31px;height:31px;border-width:2.5px}
  .card-front .brand-name{left:70px;top:35px;font-size:9.8px}
  .card-front .brand-slogan{left:70px;top:49px;font-size:6.6px;line-height:8.4px}
  .person{position:absolute;left:29px;top:94px}
  .person-name{font-size:13.5px;font-weight:700;color:var(--navy)}
  .person-role{margin-top:2px;font-size:7.4px;line-height:8.8px;color:var(--muted)}
  .person-address{margin-top:12px;font-size:7.4px;line-height:9.4px;color:var(--muted)}
  .contacts{position:absolute;left:161px;top:101px;list-style:none;font-size:7.4px;color:var(--muted)}
  .contacts li{height:16.6px;display:flex;align-items:center}
  .contacts svg{width:11px;height:11px;margin-right:7px;flex:none}
  .card-front .band{bottom:0;height:13px}

  /* Visitenkarte Rückseite */
  .card-back{left:186px;top:618px;width:303px;height:196px;background:var(--navy)}
  .card-back .brand-mark{left:128px;top:51px;width:46px;height:46px;border-color:#fff;border-width:3px}
  .card-back .brand-name{left:0;width:100%;text-align:center;top:114px;font-size:9.8px;color:#fff}
  .card-back .brand-slogan{left:0;width:100%;text-align:center;top:135px;font-size:6.6px;line-height:8.8px;color:#fff}
</style>
</head>
<body>

<!-- Briefbogen -->
<section class="sheet letter" aria-label="Briefbogen">
  <span class="brand-mark"></span>
  <div class="brand-name">KFZ-SACHVERSTÄNDIGENBÜRO LINDQVIST</div>
  <div class="brand-slogan">Ihr Sachverständiger &amp; Kfz-Techniker-Meister<br>für Kraftfahrzeugschäden und -bewertung</div>

  <div class="letter-body">
    <p>Sehr geehrter Herr Muster,</p>
    <p>Lorem ipsum dolor sit amet, consectetuer adipiscing elit, sed diam nonummy nibh euismod tincidunt ut laoreet dolore magna aliquam erat volutpat. Ut wisi enim ad minim veniam, quis nostrud exerci tation ullamcorper suscipit lobortis nisl ut aliquip ex ea commodo consequat. Duis autem vel eum iriure dolor in hendrerit in vulputate velit esse molestie consequat, vel illum dolore eu feugiat nulla facilisis at vero eros et accumsan et iusto odio dignissim qui blandit praesent luptatum zzril delenit augue duis dolore te feugait nulla facilisi.</p>
    <p>Lorem ipsum dolor sit amet, cons ectetuer adipiscing elit, sed diam nonummy nibh euismod tincidunt ut laoreet dolore magna aliquam erat volutpat. Ut wisi enim ad minim veniam, quis nostrud exerci tation ullamcorper suscipit lobortis nisl ut umsan et iusto odio dignissim qui blandit praesent luptatum zzril delenit augue duis dolore te feugait nulla facilisi.<br>Lorem ipsum dolor sit amet, cons ectetuer adipiscing elit, sed diam nonummy nibh euismod tincidunt ut laoreet dolore magna aliquam erat volutpat. Ut wisi enim ad pat.</p>
    <p class="closing">Freundliche Grüße</p>
    <p class="closing">Max Mustermann</p>
  </div>
  <div class="signature" role="img" aria-label="Handschriftliche Unterschrift von Max Mustermann"></div>

  <footer class="letter-footer">
    <div class="company">Kfz Sachverständigenbüro Lindqvist</div>
    <div class="address">Jonas Lindqvist<br>Musterstraße 01<br>12345 Musterstadt</div>
    <div class="online">
      <div><svg class="ico" width="8" height="7" viewBox="0 0 8 7"><rect x=".5" y=".5" width="7" height="6" fill="none" stroke="#283479"/><path d="M1 1.5l3 2.5 3-2.5" fill="none" stroke="#283479"/></svg>info@kfz-lindqvist.de</div>
      <div><svg class="ico" width="8" height="8" viewBox="0 0 8 8"><circle cx="4" cy="4" r="3.5" fill="none" stroke="#283479"/><path d="M.5 4h7M4 .5c-2 2-2 5 0 7M4 .5c2 2 2 5 0 7" fill="none" stroke="#283479" stroke-width=".8"/></svg>www.kfz-lindqvist.de</div>
    </div>
    <div class="phone"><svg class="ico" width="8" height="8" viewBox="0 0 8 8"><path d="M1.5.5l1.5 1.5-.8 1.2c.6 1.2 1.4 2 2.6 2.6l1.2-.8 1.5 1.5-1 1C3.5 7.5.5 4.5.5 1.5z" fill="none" stroke="#283479" stroke-width=".9"/></svg>09876/ 54321 00</div>
  </footer>

  <svg class="band" viewBox="0 0 560 12" preserveAspectRatio="none">
    <rect width="560" height="12" fill="#283479"/>
    <polygon points="489,0 560,0 560,12 483,12 493,6" fill="#3b3b3b"/>
    <polygon points="485,0 493,0 489,5" fill="#ffffff"/>
  </svg>
</section>

<!-- Visitenkarte Vorderseite -->
<section class="sheet card-front" aria-label="Visitenkarte Vorderseite">
  <span class="brand-mark"></span>
  <div class="brand-name">KFZ-SACHVERSTÄNDIGENBÜRO LINDQVIST</div>
  <div class="brand-slogan">Ihr Sachverständiger &amp; Kfz-Techniker-Meister<br>für Kraftfahrzeugschäden und -bewertung</div>

  <div class="person">
    <div class="person-name">Jonas Lindqvist</div>
    <div class="person-role">Kfz-Sachverständiger<br>Kfz-Techniker-Meister</div>
    <div class="person-address">Musterstraße 01<br>12345 Musterstadt</div>
  </div>

  <ul class="contacts">
    <li><svg viewBox="0 0 11 11"><path d="M2 1l2 2-1 1.6c.8 1.6 1.8 2.6 3.4 3.4L8 7l2 2-1.4 1.4C4.5 10.4.6 6.5.6 2.4z" fill="none" stroke="#283479" stroke-width="1.1"/></svg>0987 6543 21 00</li>
    <li><svg viewBox="0 0 11 11"><rect x="2.5" y=".6" width="6" height="9.8" rx=".6" fill="none" stroke="#283479" stroke-width="1.1"/><line x1="4.5" y1="8.6" x2="6.5" y2="8.6" stroke="#283479"/></svg>0151 98765432</li>
    <li><svg viewBox="0 0 11 11"><rect x=".6" y="1.8" width="9.8" height="7.4" fill="none" stroke="#283479" stroke-width="1.1"/><path d="M1.5 3l4 3 4-3" fill="none" stroke="#283479" stroke-width="1.1"/></svg>info@kfz-lindqvist.de</li>
    <li><svg viewBox="0 0 11 11"><circle cx="5.5" cy="5.5" r="4.9" fill="none" stroke="#283479" stroke-width="1.1"/><path d="M.6 5.5h9.8M5.5.6c-2.6 2.8-2.6 7 0 9.8M5.5.6c2.6 2.8 2.6 7 0 9.8" fill="none" stroke="#283479" stroke-width=".9"/></svg>www.kfz-lindqvist.de</li>
  </ul>

  <svg class="band" viewBox="0 0 303 13" preserveAspectRatio="none">
    <rect width="303" height="13" fill="#283479"/>
    <polygon points="231,0 303,0 303,13 226,13 235,6" fill="#3b3b3b"/>
    <polygon points="227,0 235,0 231,5" fill="#ffffff"/>
  </svg>
</section>

<!-- Visitenkarte Rückseite -->
<section class="sheet card-back" aria-label="Visitenkarte Rückseite">
  <span class="brand-mark"></span>
  <div class="brand-name">KFZ-SACHVERSTÄNDIGENBÜRO LINDQVIST</div>
  <div class="brand-slogan">Ihr Sachverständiger &amp; Kfz-Techniker-Meister<br>für Kraftfahrzeugschäden und -bewertung</div>
</section>

</body>
</html>
```